Music Poster (that is birthday gift.)

We want a rock music poster in the spirit of the old time Copperfield Lantern psychedelic posters that says, "Brackley Summer Music Festival" "July 30, 2016." Red Hook, NY. Dustin Yates is the artist. This is the 4th Annual Event. It is also Neil Brackley's 50th birthday.
Happy to answer any questions on email or live. Call Gordon at 555.381.4926

Target Market(s)

Personal gift!

Industry/Entity Type

Festival

Requirements
Must have
• Fabulous Design....

```html
<!DOCTYPE html>
<html lang="en">
<head>
<meta charset="utf-8">
<title>Brackley Summer Music Festival</title>
<link href="https://fonts.googleapis.com/css2?family=Sail&display=swap" rel="stylesheet">
<style>
  :root {
    --paper-top: #f6f6f6;
    --paper-bottom: #d9d9d9;
    --ink: #111111;
    --note-light: #c9c9c9;
    --note-dark: #5a5a5a;
    --note-edge: #3a3a3a;
  }
  html, body { margin: 0; padding: 0; overflow: hidden; background: #ffffff; }
  .poster {
    position: relative;
    width: 810px;
    height: 1200px;
    overflow: hidden;
    background: linear-gradient(180deg, var(--paper-top) 0%, var(--paper-bottom) 100%);
    font-family: "Sail", cursive;
    color: var(--ink);
  }
  .photo-strip { position: absolute; left: 0; width: 810px; display: flex; }
  .photo-strip--top { top: 0; height: 163px; }
  .photo-strip--bottom { bottom: 0; height: 162px; }
  .photo { height: 100%; }
  .photo--stage-blue { width: 249px; background: linear-gradient(160deg, #3c63c8 0%, #1a2a6e 55%, #0b0f2c 100%); }
  .photo--band-warm { width: 316px; background: linear-gradient(180deg, #4a3a22 0%, #2a2118 50%, #6b5444 100%); }
  .photo--drums-violet { width: 245px; background: linear-gradient(150deg, #3a3ad0 0%, #24207a 60%, #151045 100%); }
  .photo--guitarist-dark { width: 249px; background: linear-gradient(170deg, #3a1414 0%, #161010 60%, #2a2a2a 100%); }
  .photo--group-night { width: 314px; background: linear-gradient(180deg, #2c3a4a 0%, #1b1f26 55%, #3a3a40 100%); }
  .photo--duo-mono { width: 247px; background: linear-gradient(180deg, #3a3a3a 0%, #111111 55%, #5a5a5a 100%); }

  .line {
    position: absolute;
    left: 0;
    width: 810px;
    margin: 0;
    text-align: center;
    font-weight: 400;
    white-space: nowrap;
    line-height: 1;
  }
  .title-main { top: 238px; font-size: 50px; letter-spacing: 6px; }
  .title-sub { top: 308px; font-size: 36px; letter-spacing: 3px; }
  .date { top: 498px; font-size: 40px; letter-spacing: 4px; padding-left: 8px; }
  .place-artist { top: 676px; font-size: 40px; letter-spacing: 3px; padding-left: 12px; }
  .edition { top: 878px; font-size: 36px; letter-spacing: 4px; padding-left: 8px; }

  .note { position: absolute; }
  .note--eighth-left { left: 68px; top: 440px; width: 80px; height: 134px; }
  .note--beamed-right { left: 654px; top: 428px; width: 100px; height: 118px; }
  .note--clef-left { left: 76px; top: 798px; width: 72px; height: 186px; }
  .note--eighth-right { left: 674px; top: 818px; width: 94px; height: 166px; }
</style>
</head>
<body>
<div class="poster">
  <div class="photo-strip photo-strip--top">
    <div class="photo photo--stage-blue" role="img" aria-label="Photo of a rock band performing on an outdoor stage under blue lights"></div>
    <div class="photo photo--band-warm" role="img" aria-label="Photo of a four-piece rock band playing guitars and drums"></div>
    <div class="photo photo--drums-violet" role="img" aria-label="Photo of a drummer behind a large kit under violet lights"></div>
  </div>

  <svg width="0" height="0" style="position:absolute">
    <defs>
      <linearGradient id="chrome" x1="0" y1="0" x2="1" y2="1">
        <stop offset="0" stop-color="#d8d8d8"/>
        <stop offset="0.5" stop-color="#8a8a8a"/>
        <stop offset="1" stop-color="#4a4a4a"/>
      </linearGradient>
    </defs>
  </svg>

  <h1 class="line title-main">Brackley Summer</h1>
  <h2 class="line title-sub">Music Festival</h2>

  <svg class="note note--eighth-left" viewBox="0 0 80 134" aria-hidden="true">
    <ellipse cx="24" cy="118" rx="22" ry="15" transform="rotate(-20 24 118)" fill="url(#chrome)" stroke="#3a3a3a" stroke-width="1.5"/>
    <rect x="42" y="4" width="6" height="112" fill="url(#chrome)" stroke="#3a3a3a" stroke-width="1"/>
    <path d="M48 6 C52 30 78 44 74 80 C72 92 68 100 64 104 C70 86 68 64 48 52 Z" fill="url(#chrome)" stroke="#3a3a3a" stroke-width="1.5"/>
  </svg>

  <svg class="note note--beamed-right" viewBox="0 0 100 118" aria-hidden="true">
    <ellipse cx="20" cy="102" rx="18" ry="13" transform="rotate(-20 20 102)" fill="url(#chrome)" stroke="#3a3a3a" stroke-width="1.5"/>
    <ellipse cx="80" cy="90" rx="18" ry="13" transform="rotate(-20 80 90)" fill="url(#chrome)" stroke="#3a3a3a" stroke-width="1.5"/>
    <rect x="33" y="16" width="5" height="84" fill="url(#chrome)" stroke="#3a3a3a" stroke-width="1"/>
    <rect x="93" y="4" width="5" height="84" fill="url(#chrome)" stroke="#3a3a3a" stroke-width="1"/>
    <path d="M33 16 L98 4 L98 16 L33 28 Z" fill="url(#chrome)" stroke="#3a3a3a" stroke-width="1.5"/>
  </svg>

  <p class="line date">July 30, 2016.</p>
  <p class="line place-artist">Red Hook, NY. Dustin Yates</p>

  <svg class="note note--clef-left" viewBox="0 0 72 186" aria-hidden="true">
    <path d="M40 180 C20 182 18 160 32 160 M36 176 L36 10 C36 2 52 4 52 20 C52 44 8 64 8 104 C8 132 28 144 44 144 C64 144 70 126 66 112 C60 96 36 94 28 110 C22 122 32 132 40 130"
          fill="none" stroke="url(#chrome)" stroke-width="8" stroke-linecap="round"/>
    <path d="M40 180 C20 182 18 160 32 160 M36 176 L36 10 C36 2 52 4 52 20 C52 44 8 64 8 104 C8 132 28 144 44 144 C64 144 70 126 66 112 C60 96 36 94 28 110 C22 122 32 132 40 130"
          fill="none" stroke="#3a3a3a" stroke-width="1" stroke-linecap="round"/>
  </svg>

  <svg class="note note--eighth-right" viewBox="0 0 94 166" aria-hidden="true">
    <ellipse cx="30" cy="146" rx="27" ry="18" transform="rotate(-20 30 146)" fill="url(#chrome)" stroke="#3a3a3a" stroke-width="1.5"/>
    <rect x="52" y="4" width="7" height="140" fill="url(#chrome)" stroke="#3a3a3a" stroke-width="1"/>
    <path d="M59 6 C64 36 94 54 90 98 C88 112 84 122 78 128 C86 106 84 78 59 64 Z" fill="url(#chrome)" stroke="#3a3a3a" stroke-width="1.5"/>
  </svg>

  <p class="line edition">4th Annual Event</p>

  <div class="photo-strip photo-strip--bottom">
    <div class="photo photo--guitarist-dark" role="img" aria-label="Photo of a seated blues guitarist in a hat playing on stage"></div>
    <div class="photo photo--group-night" role="img" aria-label="Photo of four rock musicians posing together on stage"></div>
    <div class="photo photo--duo-mono" role="img" aria-label="Black and white photo of two guitarists performing on stage"></div>
  </div>
</div>
</body>
</html>
```